Business Card Design, including supply of raw art files plus a vector diagram of the flenzo logo and

We need the business card design for a company that is launching a new exciting product. The brief requires the submission of the following once the final design is chosen:

- business card layout including raw files
- a composite vector image file of the flenzo logo and tag line
- a standalone vector image file of the flenzo logo

The product will be launched as a customer engagement app.

It has 4 core modules which enables a person to do multiple things - book tours and activities, order takeaways, search for local deals and offers. A universal currency is at the heart of this product. When you use the app, you earn cashback rewards when shopping or buying at any of the merchant partners across the modules as . These rewards can then be used as full or part payment when buying goods or services at these merchant partners.

The business card must help us build the brand, communicate the benefit of the brand's key focus - the ability to earn and burn this universal cashback ccurrency - across the 4 modules - booking of tours and activities, ordering, searching for local deals and payment.

We would like the design to use the brand's blue colour the hex colour is: 00
Dark grey : 646464
Darker blue shadow: 058bdd
Main Blue: 0084ff

We need to translate this into a CMYK print or spot colour print.

Both print options to be supplied as separate files.

An example of the base concept we have in mind is attached for your reference.

The font used by the brand is Proxima Nova.

Industry/Entity Type

Business

Contact Information for Business Card

Carla Whitfield
Marketing
W: www.flenzo.co
M: + 61 407318265
T: +61 2 9375 4120
A: Suite 7, Level 2, 14-18 Harrow Lane, Sydney, NSW, 2000, Australia

Font styles to use
Sans Serif

Requirements
Must have
• flEnzo logo and tagline
• address details
• flEnzo icons as supplied
Nice to have
• would like to have the option of a spot varnish layer over the logo and icons at the back of the card

```html
<!DOCTYPE html>
<html lang="en">
<head>
<meta charset="utf-8">
<title>Flenzo Business Card</title>
<link rel="stylesheet" href="https://fonts.googleapis.com/css2?family=Open+Sans:wght@400;600;700&display=swap">
<style>
  :root {
    --stage: #2b2b2b;
    --brand-blue: #3a92d8;
    --brand-blue-deep: #0d63ad;
    --accent-blue: #1b7fd0;
    --card-white: #ffffff;
    --ink: #3a3a3a;
    --ink-soft: #646464;
    --rule: #2d2d2d;
  }
  * { box-sizing: border-box; margin: 0; padding: 0; }
  html, body { width: 1200px; height: 900px; overflow: hidden; }
  body {
    background: var(--stage);
    font-family: "Open Sans", sans-serif;
    position: relative;
  }
  .card {
    position: absolute;
    width: 540px;
    height: 310px;
    border-radius: 18px;
    overflow: hidden;
  }
  .card-back { left: 90px; top: 110px; background: var(--brand-blue); color: #fff; }
  .card-front { left: 570px; top: 480px; background: var(--card-white); color: var(--ink); }

  .brand-name { position: absolute; font-weight: 600; line-height: 1; letter-spacing: 3px; white-space: nowrap; }

  .card-back .brand-name { left: 0; right: 0; top: 118px; text-align: center; font-size: 46px; color: #fff; }

  .feature { position: absolute; display: flex; flex-direction: column; align-items: center; gap: 4px; }
  .feature-icon {
    width: 40px; height: 40px; border-radius: 50%;
    background: var(--brand-blue-deep);
    display: flex; align-items: center; justify-content: center;
  }
  .feature-label { font-size: 10px; white-space: nowrap; }
  .feature-ordering { left: 28px; top: 168px; }
  .feature-cashback { left: 96px; top: 232px; }
  .feature-tours { left: 420px; top: 22px; }
  .feature-offers { left: 452px; top: 90px; }

  .card-back .web { position: absolute; left: 0; right: 0; bottom: 22px; text-align: center; font-size: 15px; letter-spacing: 1.2px; }

  .card-front .brand-name { left: 34px; top: 62px; font-size: 40px; color: var(--ink); }

  .person { position: absolute; right: 34px; top: 58px; text-align: right; }
  .person-name { font-size: 17px; font-weight: 700; color: var(--accent-blue); letter-spacing: 0.3px; }
  .person-role { font-size: 14px; color: var(--ink); margin-top: 4px; }
  .rule { position: absolute; height: 1px; background: var(--rule); }
  .rule-top { left: 250px; right: 34px; top: 112px; }
  .rule-bottom { left: 34px; width: 220px; top: 216px; }

  .address { position: absolute; right: 34px; top: 126px; text-align: right; font-size: 12.5px; line-height: 1.45; color: var(--ink); font-style: normal; }

  .contacts { position: absolute; left: 34px; top: 228px; list-style: none; font-size: 13.5px; line-height: 1.5; color: var(--ink); }
  .contacts li { display: flex; align-items: center; gap: 8px; }
  .contact-icon { width: 14px; height: 14px; border-radius: 50%; background: var(--accent-blue); display: flex; align-items: center; justify-content: center; flex: none; }
</style>
</head>
<body>

<section class="card card-back" aria-label="Card back">
  <div class="brand-name">FLENZO</div>

  <div class="feature feature-ordering">
    <span class="feature-icon">
      <svg width="22" height="22" viewBox="0 0 22 22" fill="none" stroke="#fff" stroke-width="1.8" stroke-linecap="round">
        <path d="M5 4v5M7.5 4v5M10 4v5M5 9h5M7.5 9v10"/>
        <ellipse cx="15" cy="7" rx="2.4" ry="3.4" fill="#fff" stroke="none"/>
        <path d="M15 10v9"/>
      </svg>
    </span>
    <span class="feature-label">Mobile Ordering</span>
  </div>

  <div class="feature feature-cashback">
    <span class="feature-icon">
      <svg width="22" height="22" viewBox="0 0 22 22" fill="none" stroke="#fff" stroke-width="1.8" stroke-linecap="round">
        <path d="M4 8a7 7 0 0 1 12-3M18 14a7 7 0 0 1-12 3"/>
        <path d="M16 2v3h-3M6 20v-3h3"/>
        <path d="M13 8.5c-.5-.8-1.3-1-2-1-1.2 0-2 .6-2 1.5 0 2 4 1 4 3 0 .9-.8 1.5-2 1.5-.8 0-1.6-.3-2-1M11 6v1.5M11 13.5V15"/>
      </svg>
    </span>
    <span class="feature-label">CashBack Rewards</span>
  </div>

  <div class="feature feature-tours">
    <span class="feature-icon">
      <svg width="22" height="22" viewBox="0 0 22 22">
        <path d="M3 7h4l1.5-2h5L15 7h4v10H3z" fill="#fff"/>
        <circle cx="11" cy="12" r="3.2" fill="#0d63ad"/>
      </svg>
    </span>
    <span class="feature-label">Tours &amp; Activities</span>
  </div>

  <div class="feature feature-offers">
    <span class="feature-icon">
      <svg width="22" height="22" viewBox="0 0 22 22">
        <path d="M7 4h8l2 4v11H5V8z" fill="#fff"/>
        <circle cx="11" cy="8" r="1.4" fill="#0d63ad"/>
      </svg>
    </span>
    <span class="feature-label">Local Offers</span>
  </div>

  <div class="web">www.flenzo.co</div>
</section>

<section class="card card-front" aria-label="Card front">
  <div class="brand-name">FLENZO</div>

  <div class="person">
    <div class="person-name">CARLA WHITFIELD</div>
    <div class="person-role">Marketing</div>
  </div>
  <div class="rule rule-top"></div>

  <address class="address">
    Suite 7, Level 2,<br>
    14-18 Harrow Lane, Sydney,<br>
    NSW, 2000, Australia
  </address>

  <div class="rule rule-bottom"></div>
  <ul class="contacts">
    <li>
      <span class="contact-icon"><svg width="8" height="10" viewBox="0 0 8 10"><rect x="1.5" y="0.5" width="5" height="9" rx="1" fill="none" stroke="#fff"/></svg></span>
      + 61 407318265
    </li>
    <li>
      <span class="contact-icon"><svg width="9" height="8" viewBox="0 0 9 8"><rect x="0.5" y="2" width="8" height="5.5" rx="1" fill="#fff"/><rect x="2" y="0.5" width="5" height="2" fill="#fff"/></svg></span>
      +61 2 9375 4120
    </li>
    <li>
      <span class="contact-icon"><svg width="10" height="10" viewBox="0 0 10 10" fill="none" stroke="#fff" stroke-width="0.9"><circle cx="5" cy="5" r="4"/><ellipse cx="5" cy="5" rx="1.8" ry="4"/><path d="M1 5h8"/></svg></span>
      www.flenzo.co
    </li>
  </ul>
</section>

</body>
</html>
```